Velmarhomes.com requires a powerful call to action landing page to attract sellers in Ontario

We are a new Toronto based real estate company, starting an advertisement campaign online to get sellers and buyers.
This will be the landing page for them to view and submit their contact information.

This page should feature:
- Our Previous Sold Listings (which I will provide via email) Including high quality pictures
- An "explainer" video included on the page
- Fast to load, with high quality imaging
- A section of this page should include a contact/submit form for potential clients
- Company contact information
- Bottom of page will include testimonial videos from past clients

I would like the page to be very clean and minimalistic, I will be sending you a 2-300 word sales copy to be placed on the site.
Our design should reflect our logo colours, which will also be attached.

Our page should be elegant, luxurious looking and stand out from the competition.
Updates

Target Market(s)

Looking to target, people all over the Ontario looking to sell their homes.

Industry/Entity Type

Real Estate

Number of Pages Required

1 page

Requirements
Must have
• Header/cover to feature slide show of previous sold listings (see link below for listings) with high quality images (click virtual tour for each listing HQ images) and few details such as; rooms, bathrooms, city. Please also add a strong emphasis on listing detail such as; Days on market(DOM), List price and sold price, calculated over asking value in ($) (sold price minus list price)
• http://v3.quindrelistings.net/Live/Pages/Public/Link.aspx?Key=c493e51a88107fbe2364a9b1c6027d15&App=KPLO

```html
<!DOCTYPE html>
<html lang="en">
<head>
<meta charset="utf-8">
<title>Velmar Homes — Sell Your Home in Ontario</title>
<link href="https://fonts.googleapis.com/css2?family=Open+Sans:ital,wght@0,400;0,600;0,700;1,400;1,600&family=Oswald:wght@400&display=swap" rel="stylesheet">
<style>
:root{
  --red:#ed1c24;
  --red-dark:#b8141a;
  --ink:#333333;
  --muted:#555555;
  --page:#f3f3f3;
  --white:#ffffff;
  --line:#bdbdbd;
  --footer:#1b1919;
  --footer-text:#9a9a9a;
}
*{box-sizing:border-box;margin:0;padding:0}
html,body{width:1200px;height:2889px;overflow:hidden}
body{position:relative;background:var(--page);font-family:"Open Sans",Arial,sans-serif;color:var(--ink)}
.abs{position:absolute}

/* header */
.site-header{left:0;top:0;width:1200px;height:129px;background:var(--white)}
.brand{left:139px;top:34px;display:flex;align-items:center;gap:14px}
.brand-square{width:52px;height:52px;background:var(--red)}
.brand-name{font-size:40px;font-weight:400;color:var(--ink);letter-spacing:-0.5px}
.social{left:924px;top:10px;display:flex;gap:10px}
.social span{width:28px;height:28px;border:1.5px solid #444;border-radius:50%;display:flex;align-items:center;justify-content:center}
.phone{left:878px;top:74px;display:flex;align-items:center;gap:8px;font-family:"Oswald",Arial,sans-serif;font-size:30px;color:#222;letter-spacing:1px}

/* nav */
.main-nav{left:0;top:129px;width:1200px;height:37px;background:var(--red)}
.main-nav a{position:absolute;top:10px;color:var(--white);font-size:14px;text-decoration:none;text-transform:uppercase}

/* hero */
.hero{left:0;top:166px;width:1200px;height:452px;background:linear-gradient(100deg,#7a6a58 0%,#b39878 30%,#d8c7ae 55%,#efe7da 75%,#c9b8a0 100%)}
.hero-rule{left:0;top:618px;width:1200px;height:6px;background:#2a2a2a}
.listing-card{left:260px;top:333px;width:318px;height:212px;background:rgba(40,36,32,.72);border-radius:4px;color:var(--white);font-size:14px}
.listing-card p{position:absolute;left:16px}
.tour-btn{left:77px;top:172px;width:164px;height:28px;background:var(--red);color:var(--white);font-size:13px;display:flex;align-items:center;justify-content:center;border-radius:2px}
.slider-dots{left:560px;top:596px;display:flex;gap:10px}
.slider-dots span{width:14px;height:14px;border-radius:50%;background:var(--white)}
.slider-dots span.active{background:var(--red)}

/* welcome */
.welcome-title{left:135px;top:656px;font-size:34px;font-weight:400;color:var(--red)}
.welcome-copy{left:135px;top:712px;width:920px;font-size:13px;line-height:21.5px;color:var(--muted)}

/* video */
.video-frame{left:227px;top:886px;width:746px;height:453px;background:#e0e0e0;border:1px solid #c8c8c8}
.video-poster{left:260px;top:919px;width:680px;height:387px;background:linear-gradient(180deg,#6f9fd6 0%,#b7d0ea 35%,#8d7b6c 60%,#e9eef3 100%)}
.video-controls{left:273px;top:1267px;width:651px;height:35px;background:rgba(20,20,20,.8);border-radius:4px}

/* bands */
.band{left:0;width:1200px;height:71px;background:var(--red);color:var(--white);font-size:30px;font-weight:700;display:flex;align-items:center;justify-content:center}

/* form */
.field-label{font-size:14px;font-style:italic;font-weight:600;color:#222}
.field{background:var(--white);border:1px solid var(--line)}
.submit-btn{left:420px;top:1835px;width:360px;height:45px;background:var(--red);border-bottom:4px solid var(--red-dark);color:var(--white);font-size:15px;font-weight:600;display:flex;align-items:center;justify-content:center}

/* contact info */
.office-name{left:166px;top:2010px;font-size:22px;color:#222}
.office-line{left:166px;font-size:13px;color:#333;display:flex;gap:10px;line-height:21px}
.map{left:599px;top:1988px;width:466px;height:275px;background:linear-gradient(135deg,#e8e6dc 0%,#dfe3d8 55%,#bcd3ea 100%);border:1px solid #c8c8c8}

/* testimonial */
.quote{left:196px;top:2500px;width:545px;font-size:15px;font-style:italic;font-weight:600;line-height:22.5px;color:#222}
.client-name{left:560px;top:2640px;width:176px;text-align:right;font-size:22px;font-weight:700;color:var(--red)}
.client-city{left:560px;top:2671px;width:176px;text-align:right;font-size:14px;font-weight:600;color:#222}
.quote-dots{left:216px;top:2670px;display:flex;gap:4px}
.quote-dots span{width:11px;height:11px;background:#222}
.quote-dots span.active{background:var(--red)}
.client-ring{left:808px;top:2458px;width:232px;height:232px;border-radius:50%;background:var(--red)}
.client-photo{left:804px;top:2452px;width:228px;height:228px;border-radius:50%;background:linear-gradient(160deg,#c9cfd6,#6c7d95);border:6px solid var(--white)}

/* footer */
.site-footer{left:0;top:2758px;width:1200px;height:131px;background:var(--footer)}
.footer-nav{left:0;top:2774px;width:1200px;display:flex;justify-content:center;gap:14px;font-size:12px;color:#cfcfcf}
.footer-nav i{font-style:normal;color:#777}
.copyright{left:0;top:2808px;width:1200px;text-align:center;font-size:11px;color:#666}
</style>
</head>
<body>

<header class="abs site-header">
  <div class="abs brand"><span class="brand-square"></span><span class="brand-name">Velmar Homes</span></div>
  <div class="abs social">
    <span><svg width="14" height="10" viewBox="0 0 14 10"><rect x="0.5" y="0.5" width="13" height="9" fill="none" stroke="#444"/><path d="M0.5 0.5 7 6 13.5 0.5" fill="none" stroke="#444"/></svg></span>
    <span></span><span></span><span></span>
  </div>
  <div class="abs phone">
    <svg width="22" height="22" viewBox="0 0 24 24"><path fill="#ed1c24" d="M6.6 10.8a15 15 0 0 0 6.6 6.6l2.2-2.2c.3-.3.7-.4 1-.2 1.1.4 2.3.6 3.6.6.6 0 1 .4 1 1V20c0 .6-.4 1-1 1A17 17 0 0 1 3 4c0-.6.4-1 1-1h3.5c.6 0 1 .4 1 1 0 1.3.2 2.5.6 3.6.1.3 0 .7-.2 1z"/></svg>
    9999999XXX
  </div>
</header>

<nav class="abs main-nav">
  <a style="left:162px">Home</a>
  <a style="left:239px">About Us</a>
  <a style="left:343px">Services</a>
  <a style="left:439px">Current Listings</a>
  <a style="left:599px">Previous Sold Listings</a>
  <a style="left:803px">Contact Us</a>
</nav>

<section class="abs hero" role="img" aria-label="Photo of a sold listing's living room with leather sofa, glass table and bright windows"></section>
<div class="abs listing-card">
  <p style="top:16px">Kestrel Ontario L4R2K8 118-12-B Marwick Dr</p>
  <p style="top:51px">List: $359,900 &nbsp;&nbsp;&nbsp; Sold: $375,000</p>
  <p style="top:88px">Semi-Detached 2-Storey</p>
  <p style="top:124px">Last Status: Sld</p>
  <div class="abs tour-btn">Take A Virtual Tour</div>
</div>
<div class="abs slider-dots"><span class="active"></span><span></span><span></span><span></span></div>
<div class="abs hero-rule"></div>

<h1 class="abs welcome-title">Welcome to Velmar Homes</h1>
<p class="abs welcome-copy">Lorem ipsum dolor sit amet, consectetur adipisicing elit, sed do eiusmod tempor incididunt ut labore et dolore magna aliqua. Ut enim ad minim veniam, quis nostrud exercitation ullamco laboris nisi ut aliquip ex ea commodo consequat. Duis aute irure dolor in reprehenderit in voluptate velit esse cillum dolore eu fugiat nulla pariatur. Excepteur sint occaecat cupidatat non proident, sunt in culpa qui officia deserunt mollit anim id est laborum. Sed ut perspiciatis unde omnis iste natus error sit voluptatem accusantium doloremque laudantium, totam rem aperiam, eaque ipsa quae ab illo inventore veritatis et quasi architecto beatae vitae dicta sunt explicabo...</p>

<div class="abs video-frame"></div>
<div class="abs video-poster" role="img" aria-label="Explainer video still: brick two-storey house in winter snow"></div>
<div class="abs video-controls">
  <svg class="abs" style="left:0;top:0" width="651" height="35" viewBox="0 0 651 35">
    <rect x="4" y="4" width="50" height="27" rx="3" fill="#111"/>
    <path d="M23 11 35 17.5 23 24z" fill="#fff"/>
    <rect x="68" y="15" width="400" height="5" rx="2" fill="#555"/>
    <rect x="68" y="15" width="90" height="5" rx="2" fill="#2f9be0"/>
    <g fill="#2f9be0"><rect x="478" y="13" width="2" height="9"/><rect x="483" y="13" width="2" height="9"/><rect x="488" y="13" width="2" height="9"/><rect x="493" y="13" width="2" height="9"/><rect x="498" y="13" width="2" height="9"/></g>
    <text x="510" y="22" font-family="Open Sans,Arial,sans-serif" font-size="11" font-weight="700" font-style="italic" fill="#2f9be0">HD</text>
    <path d="M540 12l6 6m0-6l-6 6" stroke="#ccc" stroke-width="2"/>
  </svg>
</div>

<h2 class="abs band" style="top:1389px">CONTACT US</h2>

<form>
  <label class="abs field-label" style="left:212px;top:1496px">Name:</label>
  <div class="abs field" style="left:212px;top:1516px;width:362px;height:42px"></div>
  <label class="abs field-label" style="left:630px;top:1496px">Phone:</label>
  <div class="abs field" style="left:630px;top:1516px;width:362px;height:42px"></div>
  <label class="abs field-label" style="left:212px;top:1573px">Email:</label>
  <div class="abs field" style="left:212px;top:1593px;width:362px;height:42px"></div>
  <label class="abs field-label" style="left:630px;top:1573px">Subject:</label>
  <div class="abs field" style="left:630px;top:1593px;width:362px;height:42px"></div>
  <label class="abs field-label" style="left:212px;top:1660px">Message:</label>
  <div class="abs field" style="left:212px;top:1679px;width:780px;height:122px"></div>
  <div class="abs submit-btn">CONTACT NOW</div>
</form>

<h3 class="abs office-name">Velmar Homes</h3>
<div class="abs office-line" style="top:2058px">
  <svg width="12" height="18" viewBox="0 0 12 18"><path d="M6 1a5 5 0 0 0-5 5c0 4 5 11 5 11s5-7 5-11a5 5 0 0 0-5-5z" fill="none" stroke="#666"/><circle cx="6" cy="6" r="2" fill="#666"/></svg>
  <span>Lorem ipsum dolor sit amet, consectetur<br>adipisicing elit, sed do eiusmod tempor<br>incididunt ut labore et dolore.</span>
</div>
<div class="abs office-line" style="top:2134px">
  <svg width="14" height="14" viewBox="0 0 24 24"><path fill="#666" d="M6.6 10.8a15 15 0 0 0 6.6 6.6l2.2-2.2c.3-.3.7-.4 1-.2 1.1.4 2.3.6 3.6.6.6 0 1 .4 1 1V20c0 .6-.4 1-1 1A17 17 0 0 1 3 4c0-.6.4-1 1-1h3.5c.6 0 1 .4 1 1 0 1.3.2 2.5.6 3.6.1.3 0 .7-.2 1z"/></svg>
  <span>9999 999 999</span>
</div>
<div class="abs office-line" style="top:2176px">
  <svg width="14" height="14" viewBox="0 0 14 14"><rect x="1" y="5" width="12" height="6" fill="none" stroke="#666"/><rect x="3.5" y="1.5" width="7" height="3.5" fill="none" stroke="#666"/><rect x="3.5" y="9" width="7" height="4" fill="#666"/></svg>
  <span>9999 999 999</span>
</div>
<div class="abs office-line" style="top:2215px">
  <svg width="14" height="12" viewBox="0 0 14 12"><rect x="0.5" y="1.5" width="13" height="9" fill="none" stroke="#666"/><path d="M0.5 1.5 7 7 13.5 1.5" fill="none" stroke="#666"/></svg>
  <span>info@Velmarhomes.com</span>
</div>
<div class="abs map" role="img" aria-label="Street map of the Toronto area with the office location pinned"></div>

<h2 class="abs band" style="top:2346px">WHAT SAYING HAPPY CLIENT</h2>

<svg class="abs" style="left:194px;top:2495px" width="18" height="16" viewBox="0 0 18 16"><path d="M1 15V9C1 4 3 1 7 0v3C5 4 4 6 4 8h3v7zM10 15V9c0-5 2-8 6-9v3c-2 1-3 3-3 5h3v7z" fill="#222"/></svg>
<blockquote class="abs quote" style="left:216px;width:525px">Lorem ipsum dolor sit amet, consectetur adipisicing elit, sed do eiusmod tempor incididunt ut labore et dolore magna aliqua. Ut enim ad minimyi veniam, quis nostrud exercitation ullamco laboris nisi ut aliquip ex eahd commodo consequat. Duis aute irure dolor in reprehenderit in voluptate velit esse cillum dolore eu fugiat nulla pariatur. Excepteur sint occaecat cupidatat non proident..</blockquote>
<svg class="abs" style="left:392px;top:2614px" width="18" height="16" viewBox="0 0 18 16"><path d="M17 1v6c0 5-2 8-6 9v-3c2-1 3-3 3-5h-3V1zM8 1v6c0 5-2 8-6 9v-3c2-1 3-3 3-5H2V1z" fill="#222"/></svg>
<p class="abs client-name">- Daniel R.</p>
<p class="abs client-city">Toronto</p>
<div class="abs quote-dots"><span class="active"></span><span></span><span></span><span></span><span></span></div>
<div class="abs client-ring"></div>
<div class="abs client-photo" role="img" aria-label="Portrait photo of the client giving the testimonial"></div>

<footer class="abs site-footer"></footer>
<nav class="abs footer-nav">
  <span>Home</span><i>|</i><span>About Us</span><i>|</i><span>Services</span><i>|</i><span>Current Listings</span><i>|</i><span>Previous Sold Listings</span><i>|</i><span>Contact Us</span>
</nav>
<p class="abs copyright">Copyright © 2015 Velmarhomes.com. All rights reserved.</p>

</body>
</html>
```